Web site for Life Coaching Consultant

I require a website for a life coaching business. I have a Velvo Hosting account which I set up last week. I will need to be able to add articles and testimonials. The design should communicate that KT Amber Lantern is there to help people breakdown personal barriers and that we are an advocate to help them achieve personal goals.
Updates

Reason: I have some designers just accepting my invitation to submit so to give them a few days to submit. I have been thrilled with the quality of the submissions Thank you.

Hi everyone

I am loving all your designs.  The only feedback I can get from people is that they feel that the runner makes the web page look like a personal coach rather than a life coach that helps people with relations, career, and personal road blocks.

Sorry                                   

Reason: Hi I have increased the deadline as there has been so many amazing designs and some of you have asked to fine tune your entries. I would like to take this opportunity to thank you all. It is going to be a tough decision. I have put a few more pictures on the project page hoping this will help

Hi I just wanted to thank you all for your great designs.  As I got so many good designs I have asked people to vote.  I will be in touch in the next day or 2.

Cheers

Target Market(s)

People with self esteem issues either woman or girls, people who want to goal set and need an advocate

Industry/Entity Type

Life Coaching

Colors
d2a4cc
e567a6

Requirements
Must have
• must have bio section, logo, articles page, affirmation section and testimonial page.

```html
<!DOCTYPE html>
<html lang="en">
<head>
<meta charset="utf-8">
<title>KT Amber Lantern – Life Coaching</title>
<link rel="stylesheet" href="https://fonts.googleapis.com/css2?family=Source+Sans+3:wght@400;600;700&display=swap">
<style>
:root{
  --pink:#eb1f7b;
  --pink-dark:#b3185f;
  --pink-deep:#9c1452;
  --ink:#3a3a3a;
  --muted:#5a5a5a;
  --page:#f7f7f7;
  --white:#ffffff;
  --rule:#d9d9d9;
  --list-bg:#ececec;
}
*{box-sizing:border-box;margin:0;padding:0}
html,body{width:984px;height:1200px;overflow:hidden;background:var(--page)}
body{font-family:"Source Sans 3",sans-serif;color:var(--ink);position:relative}
.abs{position:absolute}

/* header */
.header{left:0;top:0;width:984px;height:106px}
.nav-band{left:0;top:70px;width:984px;height:36px;background:var(--pink)}
.brand-disc{left:124px;top:6px;width:88px;height:88px;border-radius:50%;background:var(--white);border:4px solid var(--pink)}
.brand-name{left:218px;top:28px;font-size:26px;font-weight:700;color:var(--pink);white-space:nowrap}
.phone{left:222px;top:78px;color:var(--white);font-size:13px;font-weight:600;display:flex;align-items:center;gap:6px}
.search{left:622px;top:22px;width:236px;height:29px;border:1px solid var(--pink);border-radius:4px;background:var(--white);overflow:hidden}
.search span{position:absolute;left:12px;top:6px;font-size:11px;color:var(--muted)}
.search .btn{position:absolute;right:0;top:0;width:39px;height:27px;background:var(--pink);display:flex;align-items:center;justify-content:center}
.menu{left:381px;top:70px;height:36px;display:flex}
.menu a{display:block;height:36px;line-height:36px;padding:0 16px;color:var(--white);font-size:12px;text-decoration:none}
.menu a.current{background:var(--pink-dark);padding:0 21px}

/* hero */
.hero{left:0;top:106px;width:984px;height:350px;background:linear-gradient(90deg,#e4e0cf 0%,#f1efe4 40%,#dfe8ee 70%,#e9eef0 100%)}
.hero-band{left:0;top:456px;width:984px;height:7px;background:var(--pink-dark)}
.hero-person{left:470px;top:106px;width:360px;height:350px;background:linear-gradient(180deg,#c9d6e4 0%,#a9c2dc 100%);opacity:.8}
.hero-title{left:134px;top:200px;font-size:40px;line-height:40px;font-weight:700;color:var(--pink);white-space:nowrap}
.hero-title span{display:block;padding-left:25px}
.hero-rule{left:145px;top:291px;width:235px;height:1px;background:var(--pink)}
.hero-sub{left:173px;top:300px;font-size:11px;line-height:17px;font-weight:700;color:var(--pink)}
.hero-cta{left:344px;top:367px;width:93px;height:26px;background:var(--pink);border-radius:3px;color:var(--white);font-size:11px;font-weight:700;text-align:center;line-height:26px}
.arrow{width:50px;height:50px;border-radius:50%;display:flex;align-items:center;justify-content:center}
.arrow.prev{left:69px;top:256px;background:var(--pink)}
.arrow.next{left:866px;top:256px;border:1px solid var(--pink)}
.dots{left:796px;top:429px;display:flex;gap:4px}
.dots i{width:14px;height:14px;border-radius:50%;border:1px solid var(--white)}
.dots i.on{background:var(--pink);border-color:var(--pink)}

/* topics */
.topic{top:499px;width:172px}
.topic .photo{height:116px;border:1px solid #cfcfcf;border-bottom:3px solid var(--pink);border-radius:3px}
.topic h3{margin-top:8px;font-size:17px;font-weight:600;color:var(--pink);padding:0 1px 4px;border-bottom:1px solid var(--pink)}
.topic p{margin-top:6px;font-size:9px;line-height:15.6px;color:var(--muted);padding-right:4px}
.readmore{display:inline-block;height:23px;line-height:21px;padding:0 12px;border:1px solid var(--pink);border-radius:3px;color:var(--pink);font-size:9px;font-weight:600;background:var(--white)}
.readmore.solid{background:var(--pink);color:var(--white)}
.topic .readmore{margin-top:14px}
.divider{left:0;top:812px;width:984px;height:1px;background:#cccccc}

/* welcome */
.welcome-title{left:126px;top:838px;font-size:19px;color:var(--ink)}
.welcome-title b{color:var(--pink);font-weight:700}
.welcome-photo{left:126px;top:884px;width:172px;height:156px;border:1px solid #cfcfcf;border-radius:3px;background:linear-gradient(180deg,#dfe6ec 0%,#9aa7b3 100%)}
.welcome-text{left:314px;top:882px;width:320px;font-size:9px;line-height:15.6px;color:var(--muted)}
.welcome-text p+p{margin-top:15px}
.welcome-more{left:313px;top:1018px}

/* sidebar */
.side-title{left:686px;top:838px;font-size:19px;color:var(--ink)}
.side-rule{left:686px;top:867px;width:172px;height:1px;background:var(--pink)}
.side-list{left:686px;top:872px;width:172px;list-style:none}
.side-list li{height:23px;margin-bottom:3.5px;background:var(--list-bg);font-size:11px;line-height:23px;padding-left:30px;position:relative;color:var(--ink)}
.side-list li::before{content:"";position:absolute;left:14px;top:8px;width:5px;height:5px;border-right:1.5px solid currentColor;border-bottom:1.5px solid currentColor;transform:rotate(-45deg)}
.side-list li.active{background:var(--pink);color:var(--white)}

/* footer */
.footer{left:0;top:1111px;width:984px;height:65px;background:var(--pink)}
.footer-disc{left:134px;top:1092px;width:60px;height:60px;border-radius:50%;background:var(--white);border:4px solid var(--pink)}
.footer-name{left:112px;top:1148px;font-size:15px;font-weight:700;color:var(--white);white-space:nowrap}
.contact{left:250px;top:1119px;font-size:11px;line-height:17.5px;color:var(--white);font-weight:600}
.contact dt{float:left;width:47px;clear:left;font-weight:400}
.contact dd{margin-left:47px}
.social{left:741px;top:1133px;display:flex;gap:9px}
.social i{width:23px;height:23px;border-radius:50%;background:var(--white)}
.copy{left:0;top:1176px;width:984px;height:24px;background:var(--pink-deep);color:var(--white);font-size:9.5px;line-height:24px;padding-left:125px;font-weight:600}
</style>
</head>
<body>

<header class="abs header">
  <div class="abs nav-band"></div>
  <div class="abs brand-disc"></div>
  <div class="abs brand-name">Amber Lantern</div>
  <div class="abs phone">
    <svg width="9" height="15" viewBox="0 0 9 15"><rect x="0.8" y="0.8" width="7.4" height="13.4" rx="1.3" fill="none" stroke="#fff" stroke-width="1.5"/><circle cx="4.5" cy="11.6" r="0.9" fill="#fff"/></svg>
    0400 555 318
  </div>
  <div class="abs search">
    <span>Search here....</span>
    <div class="btn"><svg width="13" height="13" viewBox="0 0 13 13"><circle cx="5.3" cy="5.3" r="4" fill="none" stroke="#fff" stroke-width="2"/><line x1="8.3" y1="8.3" x2="12" y2="12" stroke="#fff" stroke-width="2.2" stroke-linecap="round"/></svg></div>
  </div>
  <nav class="abs menu">
    <a class="current">Home</a><a>Life Coaching</a><a>Our Articles</a><a>Testimonials</a><a>About us</a><a>Contact</a>
  </nav>
</header>

<section>
  <div class="abs hero" role="img" aria-label="Bright kitchen interior, softly blurred"></div>
  <div class="abs hero-person" role="img" aria-label="Smiling woman holding an open laptop"></div>
  <h1 class="abs hero-title">A Useful Guide to<span>Work Life Balance</span></h1>
  <div class="abs hero-rule"></div>
  <p class="abs hero-sub">Lorem ipsum dolor sit amet, consectetur adipisicing<br>elit, sed do eiusmod tempor incididunt aliqua.</p>
  <div class="abs hero-cta">START TODAY</div>
  <div class="abs arrow prev"><svg width="14" height="18" viewBox="0 0 14 18"><polyline points="10,2 3,9 10,16" fill="none" stroke="#fff" stroke-width="3"/></svg></div>
  <div class="abs arrow next"><svg width="14" height="18" viewBox="0 0 14 18"><polyline points="4,2 11,9 4,16" fill="none" stroke="#eb1f7b" stroke-width="3"/></svg></div>
  <div class="abs dots"><i class="on"></i><i></i><i></i><i></i></div>
  <div class="abs hero-band"></div>
</section>

<section>
  <article class="abs topic" style="left:126px">
    <div class="photo" role="img" aria-label="Colleagues working together at an office desk" style="background:linear-gradient(180deg,#b9c3c9,#5d6670)"></div>
    <h3>Work &amp; Career</h3>
    <p>Lorem ipsum dolor sit amet, consectetur adipisicing elit, sed do eiusmod tempor incididunt ut labore et dolore magna aliqua. Ut enim ad minim veniam, quis nostrud exercitation ullamco laboris nisi ut aliquip ex ea commodo consequat.</p>
    <span class="readmore solid">Read more</span>
  </article>
  <article class="abs topic" style="left:313px">
    <div class="photo" role="img" aria-label="Happy couple embracing in a kitchen" style="background:linear-gradient(180deg,#eef0ee,#c9cfd6)"></div>
    <h3>Love &amp; Relationships</h3>
    <p>Lorem ipsum dolor sit amet, consectetur adipisicing elit, sed do eiusmod tempor incididunt ut labore et dolore magna aliqua. Ut enim ad minim veniam, quis nostrud exercitation ullamco laboris nisi ut aliquip ex ea commodo consequat.</p>
    <span class="readmore">Read more</span>
  </article>
  <article class="abs topic" style="left:500px">
    <div class="photo" role="img" aria-label="Family outdoors in autumn" style="background:linear-gradient(180deg,#c7b79a,#7c6a55)"></div>
    <h3>Home &amp; Family</h3>
    <p>Lorem ipsum dolor sit amet, consectetur adipisicing elit, sed do eiusmod tempor incididunt ut labore et dolore magna aliqua. Ut enim ad minim veniam, quis nostrud exercitation ullamco laboris nisi ut aliquip ex ea commodo consequat.</p>
    <span class="readmore">Read more</span>
  </article>
  <article class="abs topic" style="left:687px">
    <div class="photo" role="img" aria-label="Woman with arms raised by the sea" style="background:linear-gradient(180deg,#3f86b8,#a9cfe0)"></div>
    <h3>Life &amp; Living</h3>
    <p>Lorem ipsum dolor sit amet, consectetur adipisicing elit, sed do eiusmod tempor incididunt ut labore et dolore magna aliqua. Ut enim ad minim veniam, quis nostrud exercitation ullamco laboris nisi ut aliquip ex ea commodo consequat.</p>
    <span class="readmore">Read more</span>
  </article>
  <div class="abs divider"></div>
</section>

<section>
  <h2 class="abs welcome-title">Welcome to our <b>KT Amber Lantern</b></h2>
  <div class="abs welcome-photo" role="img" aria-label="Business team reviewing a document together"></div>
  <div class="abs welcome-text">
    <p>Lorem ipsum dolor sit amet, consectetur adipisicing elit, sed do eiusmod tempor incididunt ut labore et dolore magna aliqua. Ut enim ad minim veniam, quis nostrud exercitation ullamco laboris nisi ut aliquip ex ea commodo consequat. Duis aute irure dolor in reprehenderit in voluptate velit esse cillum dolore eu fugiat nulla pariatur.</p>
    <p>Duis aute irure dolor in reprehenderit in voluptate velit esse cillum dolore eu fugiat nulla pariatur.</p>
  </div>
  <span class="abs readmore solid welcome-more">Read more</span>

  <h2 class="abs side-title">Self Help Articles</h2>
  <div class="abs side-rule"></div>
  <ul class="abs side-list">
    <li>Past Predicts Future?</li>
    <li class="active">The Time Of Your Life</li>
    <li>How to Find Love</li>
    <li>Self Test</li>
    <li>Your True Purpose</li>
    <li>Past Predicts Future?</li>
    <li>The Time Of Your Life</li>
  </ul>
</section>

<footer>
  <div class="abs footer"></div>
  <div class="abs footer-disc"></div>
  <div class="abs footer-name">Amber Lantern</div>
  <dl class="abs contact">
    <dt>Phone:</dt><dd>0400 555 318</dd>
    <dt>Email:</dt><dd>hello@amberlantern.example</dd>
    <dt>Address:</dt><dd>PO Box 1204 Harbourview VIC 3100</dd>
  </dl>
  <div class="abs social"><i></i><i></i><i></i><i></i></div>
  <div class="abs copy">Copyrights © 2014 &nbsp;|&nbsp; Amber Lantern</div>
</footer>

</body>
</html>
```